Cosmetics range packaging

Needing cosmetics logo design with our logo attached and showing you some examples of products we need logo and packaging (cosmetic box) designs.
Products e.g. palette is black so the printing would be a red metallic foil on the lid of the palette as a preference / guide. With the logo it would need to get a white letter M and a red metallic foil star. This is needed for the palette lid and also for the cardboard box packaging.

Some examples of the palette packaging and shape are attached below (competitor brands) just to show you what the shape is.

Target Market(s)

Women 15-60 years of age

Industry/Entity Type

Cosmetics

Requirements
Must have
• Our logo on it and packaging background is black.
Nice to have
• The logo preferably white letter M and red foil metallic star.
Should not have
• Open to ideas

```html
<!DOCTYPE html>
<html lang="en">
<head>
<meta charset="utf-8">
<title>Palette Box Lid</title>
<link rel="stylesheet" href="https://fonts.googleapis.com/css2?family=Lato:wght@300&display=swap">
<style>
  :root {
    --page-bg: #ffffff;
    --lid-black: #030303;
    --band-deep: #2a0000;
    --band-red: #8a0000;
    --band-line: #5a0000;
    --logo-white: #e6e6e6;
    --caption-grey: #9a9a9a;
  }
  html, body {
    margin: 0;
    width: 1200px;
    height: 897px;
    overflow: hidden;
    background: var(--page-bg);
  }
  .canvas {
    position: relative;
    width: 1200px;
    height: 897px;
  }
  .box-lid {
    position: absolute;
    left: 250px;
    top: 210px;
    width: 700px;
    height: 460px;
    background: var(--lid-black);
  }
  .band {
    position: absolute;
    left: 0;
    right: 0;
    top: 150px;
    height: 86px;
  }
  .band svg { display: block; width: 100%; height: 100%; }
  .brand-plate {
    position: absolute;
    left: 50%;
    top: 150px;
    transform: translateX(-50%);
    height: 86px;
    padding: 0 26px;
    display: flex;
    align-items: center;
    gap: 12px;
    background: var(--lid-black);
  }
  .brand-dot {
    width: 14px;
    height: 14px;
    border-radius: 50%;
    background: var(--band-red);
  }
  .brand-name {
    font-family: "Lato", sans-serif;
    font-weight: 300;
    font-size: 34px;
    letter-spacing: 4px;
    color: var(--logo-white);
  }
  .caption {
    position: absolute;
    left: 0;
    right: 0;
    top: 330px;
    text-align: center;
    font-family: "Lato", sans-serif;
    font-weight: 300;
    font-size: 20px;
    color: var(--caption-grey);
    letter-spacing: 0.5px;
  }
</style>
</head>
<body>
  <main class="canvas">
    <section class="box-lid">
      <div class="band">
        <svg viewBox="0 0 700 86" preserveAspectRatio="none" aria-hidden="true">
          <defs>
            <linearGradient id="bandFill" x1="0" x2="1" y1="0" y2="0">
              <stop offset="0" stop-color="var(--band-deep)"/>
              <stop offset="0.5" stop-color="var(--band-red)"/>
              <stop offset="1" stop-color="var(--band-deep)"/>
            </linearGradient>
          </defs>
          <rect x="0" y="0" width="700" height="2" fill="var(--band-line)"/>
          <rect x="0" y="10" width="700" height="66" fill="url(#bandFill)"/>
          <rect x="0" y="84" width="700" height="2" fill="var(--band-line)"/>
        </svg>
      </div>
      <div class="brand-plate">
        <span class="brand-dot"></span>
        <span class="brand-name">MARVESSA</span>
      </div>
      <p class="caption">35 COLOR PALETTE</p>
    </section>
  </main>
</body>
</html>
```